Bellwether Guild Forum Powerpoint Template

We need a Powerpoint template to use for a professional association called the Bellwether Guild Forum. The design should incorporate a logo that we will attach. We're looking for something clean, elegant, and professional. I'm attaching a sample Powerpoint file with 2 slides of content that we'd like to have designed so that they look good and incorporate the logo. The intention is that we can then take that template and create more content on our own.

Font styles to use
Sans Serif

```html
<!DOCTYPE html>
<html lang="en">
<head>
<meta charset="utf-8">
<title>Bellwether Guild Forum – Presentation Template</title>
<link rel="stylesheet" href="https://fonts.googleapis.com/css2?family=Ubuntu:wght@400;500;700&display=swap">
<style>
:root{
  --navy:#07306e;
  --deep:#0a3a8f;
  --blue:#0f62bd;
  --bright:#1a7bd0;
  --sky:#3d9be0;
  --ink:#222831;
  --grey:#5d6470;
  --rule:#d9dde3;
  --stage-top:#e6e6e6;
  --stage-bottom:#c6c6c6;
  --white:#ffffff;
}
*{box-sizing:border-box;margin:0;padding:0}
html,body{width:1200px;height:3166px;overflow:hidden}
body{font-family:"Ubuntu",Arial,sans-serif;color:var(--ink);background:linear-gradient(var(--stage-top),var(--stage-bottom))}
.canvas{position:relative;width:1200px;height:3166px;overflow:hidden}

.slide{position:absolute;width:541px;height:303px;overflow:hidden;background:var(--white)}
.slide > *{position:absolute}
.hero{transform-origin:0 0;box-shadow:0 14px 30px rgba(0,0,0,.25)}

.dark{background:radial-gradient(circle at 70% 30%,#1560c4 0%,var(--deep) 55%,var(--navy) 100%);color:var(--white)}
.photo-tint{background:linear-gradient(100deg,#0c47a8 0%,#2f6fc0 45%,#8fb2d8 75%,#b9c9dc 100%);color:var(--white)}

.brand{display:flex;flex-direction:column;align-items:flex-start;gap:6px}
.brand .dot{width:22px;height:22px;border-radius:50%;background:var(--blue);margin-left:26px}
.dark .brand .dot,.photo-tint .brand .dot{background:var(--white)}
.brand .name{font-size:6px;font-weight:700;letter-spacing:.2px;text-transform:uppercase;color:var(--blue)}
.dark .brand .name,.photo-tint .brand .name{color:var(--white)}

.title{font-weight:700;font-size:32px;line-height:1.04;color:var(--deep);letter-spacing:-.3px}
.dark .title,.photo-tint .title{color:var(--white)}
.subtitle{font-size:16px;line-height:1.05;color:var(--bright)}
.dark .subtitle,.photo-tint .subtitle{color:var(--white)}
.date{font-size:8px;color:var(--ink)}
.dark .date,.photo-tint .date{color:var(--white)}

.deco{top:0;left:0;width:541px;height:303px}
.mark{width:22px;height:22px;border-radius:50%;background:var(--blue);top:18px;right:18px}
.page-no{width:8px;height:8px;background:var(--blue);right:12px;bottom:10px}

.heading{font-size:20px;left:24px;top:26px;color:var(--ink)}
.heading b{font-weight:500;color:var(--blue)}
.body-text{font-size:7.5px;line-height:1.15;color:var(--ink)}

/* Table of contents */
.toc-item{display:flex;gap:10px;width:170px}
.toc-item .num{font-size:19px;color:#b4b9c1;width:14px;text-align:right;line-height:1}
.toc-item .t{font-size:11px;color:var(--blue);font-weight:500}
.toc-item p{font-size:6px;line-height:1.1;color:var(--grey)}

/* About */
.about-label{font-size:14px;color:var(--blue)}
.about-name{font-size:19px;font-weight:700;line-height:1.05;color:var(--ink)}

/* How */
.how-band{right:0;top:0;width:118px;height:303px;background:var(--blue)}
.how-heading{font-size:20px;color:var(--ink)}
.how-heading b{color:var(--blue);font-weight:700}
.how-list{list-style:none;width:200px}
.how-list li{font-size:8.4px;line-height:1.1;color:var(--ink);padding-left:10px;position:relative;margin-bottom:10px}
.how-list li::before{content:"";position:absolute;left:0;top:3px;width:4px;height:4px;border-radius:50%;background:var(--blue)}

/* Features */
.feature{width:150px}
.feature h4{font-size:11px;font-weight:400;color:var(--blue);margin-bottom:2px}
.feature p{font-size:6.3px;line-height:1.15;color:var(--grey)}
.feature.right-align{text-align:right}
.icon-disc{width:36px;height:36px;border-radius:50%;background:var(--blue);display:flex;align-items:center;justify-content:center}

/* Table */
.partner-table{left:20px;top:66px;width:501px;border-collapse:collapse;font-size:5.6px;line-height:1.15;color:var(--ink)}
.partner-table th{background:var(--blue);color:var(--white);font-weight:400;font-size:8.5px;text-align:left;padding:6px 4px;border-right:1px solid var(--white)}
.partner-table td{padding:4px 4px;height:29.5px;border-bottom:1px solid var(--rule);vertical-align:middle}
.partner-table tr:nth-child(even) td{background:#f1f3f6}
.partner-table td:first-child{font-weight:500}

/* Spectrum */
.spec-label{font-size:7.5px;line-height:1.1;color:var(--grey);text-align:center;width:110px}
.vendor{font-size:11px;font-weight:700;color:var(--deep);letter-spacing:.8px}

/* Steps */
.step{width:90px;text-align:center}
.step h4{font-size:11.5px;font-weight:400;line-height:1.05;color:var(--blue);margin-bottom:8px}
.step p{font-size:7px;line-height:1.15;color:var(--ink)}
.step-disc{width:36px;height:36px;border-radius:50%;background:var(--white);border:2px solid var(--blue);color:var(--blue);font-size:18px;display:flex;align-items:center;justify-content:center}

/* Contact */
.contact-h{font-size:13px;font-weight:500}
.contact-line{display:flex;align-items:center;gap:7px;font-size:7.5px}
</style>
</head>
<body>
<main class="canvas">

  <!-- Showcase pair -->
  <section class="slide dark hero" style="left:60px;top:70px;transform:scale(1.2)">
    <svg class="deco" viewBox="0 0 541 303"><circle cx="570" cy="350" r="170" fill="#1a73c9" stroke="#fff" stroke-width="22"/></svg>
    <div class="brand" style="left:43px;top:34px"><span class="dot"></span><span class="name">Bellwether Guild Forum</span></div>
    <h1 class="title" style="left:43px;top:118px">Presentation<br>Title Goes Here!</h1>
    <p class="subtitle" style="left:43px;top:196px">Subtitle of Presentation<br>Goes Here!</p>
    <p class="date" style="left:43px;top:254px">Wednesday, April 14, 2021</p>
  </section>
  <section class="slide hero" style="left:560px;top:300px;transform:scale(1.07)">
    <svg class="deco" viewBox="0 0 541 303"><circle cx="570" cy="350" r="170" fill="#1a73c9" stroke="#07306e" stroke-width="22"/></svg>
    <div class="brand" style="left:43px;top:34px"><span class="dot"></span><span class="name">Bellwether Guild Forum</span></div>
    <h1 class="title" style="left:43px;top:118px">Presentation<br>Title Goes Here!</h1>
    <p class="subtitle" style="left:43px;top:196px">Subtitle of Presentation<br>Goes Here!</p>
    <p class="date" style="left:43px;top:254px">Wednesday, April 14, 2021</p>
  </section>

  <!-- Row 1 -->
  <section class="slide dark" style="left:50px;top:863px">
    <svg class="deco" viewBox="0 0 541 303"><circle cx="570" cy="350" r="170" fill="#1a73c9" stroke="#fff" stroke-width="22"/></svg>
    <div class="brand" style="left:43px;top:34px"><span class="dot"></span><span class="name">Bellwether Guild Forum</span></div>
    <h1 class="title" style="left:43px;top:118px">Presentation<br>Title Goes Here!</h1>
    <p class="subtitle" style="left:43px;top:196px">Subtitle of Presentation<br>Goes Here!</p>
    <p class="date" style="left:43px;top:254px">Wednesday, April 14, 2021</p>
  </section>
  <section class="slide photo-tint" style="left:609px;top:863px" role="img" aria-label="Photo of a business handshake under a blue tint">
    <svg class="deco" viewBox="0 0 541 303"><circle cx="570" cy="350" r="170" fill="#1a73c9" fill-opacity=".55" stroke="#fff" stroke-width="22"/></svg>
    <div class="brand" style="left:43px;top:34px"><span class="dot"></span><span class="name">Bellwether Guild Forum</span></div>
    <h1 class="title" style="left:43px;top:118px">Presentation<br>Title Goes Here!</h1>
    <p class="subtitle" style="left:43px;top:196px">Subtitle of Presentation<br>Goes Here!</p>
    <p class="date" style="left:43px;top:254px">Wednesday, April 14, 2021</p>
  </section>

  <!-- Row 2 -->
  <section class="slide" style="left:50px;top:1184px">
    <svg class="deco" viewBox="0 0 541 303"><circle cx="570" cy="350" r="170" fill="#1a73c9" stroke="#07306e" stroke-width="22"/></svg>
    <div class="brand" style="left:43px;top:34px"><span class="dot"></span><span class="name">Bellwether Guild Forum</span></div>
    <h1 class="title" style="left:43px;top:118px">Presentation<br>Title Goes Here!</h1>
    <p class="subtitle" style="left:43px;top:196px">Subtitle of Presentation<br>Goes Here!</p>
    <p class="date" style="left:43px;top:254px">Wednesday, April 14, 2021</p>
  </section>
  <section class="slide" style="left:609px;top:1184px">
    <svg class="deco" viewBox="0 0 541 303"><circle cx="585" cy="152" r="115" fill="#1a73c9" stroke="#07306e" stroke-width="16"/></svg>
    <div class="brand" style="left:43px;top:34px"><span class="dot"></span><span class="name">Bellwether Guild Forum</span></div>
    <h1 class="title" style="left:43px;top:118px">Presentation<br>Title Goes Here!</h1>
    <p class="subtitle" style="left:43px;top:196px">Subtitle of Presentation<br>Goes Here!</p>
    <p class="date" style="left:43px;top:254px">Wednesday, April 14, 2021</p>
  </section>

  <!-- Row 3 -->
  <section class="slide" style="left:50px;top:1506px">
    <svg class="deco" viewBox="0 0 541 303"><circle cx="-35" cy="157" r="115" fill="#1a73c9" stroke="#07306e" stroke-width="16"/></svg>
    <div class="brand" style="left:178px;top:34px"><span class="dot"></span><span class="name">Bellwether Guild Forum</span></div>
    <h1 class="title" style="left:178px;top:118px">Presentation<br>Title Goes Here!</h1>
    <p class="subtitle" style="left:178px;top:196px">Subtitle of Presentation<br>Goes Here!</p>
    <p class="date" style="left:178px;top:254px">Wednesday, April 14, 2021</p>
  </section>
  <section class="slide" style="left:609px;top:1506px">
    <svg class="deco" viewBox="0 0 541 303"><circle cx="570" cy="10" r="150" fill="#1a73c9" stroke="#07306e" stroke-width="18"/></svg>
    <div class="brand" style="left:43px;top:34px"><span class="dot"></span><span class="name">Bellwether Guild Forum</span></div>
    <h1 class="title" style="left:43px;top:118px">Presentation<br>Title Goes Here!</h1>
    <p class="subtitle" style="left:43px;top:196px">Subtitle of Presentation<br>Goes Here!</p>
    <p class="date" style="left:43px;top:254px">Wednesday, April 14, 2021</p>
  </section>

  <!-- Row 4: contents + about -->
  <section class="slide" style="left:50px;top:1828px">
    <svg class="deco" viewBox="0 0 541 303"><circle cx="40" cy="370" r="180" fill="#1a73c9" stroke="#07306e" stroke-width="20"/></svg>
    <h2 class="heading" style="font-size:21px">Table of <b>Contents</b></h2>
    <span class="mark"></span>
    <div class="toc-item" style="left:118px;top:86px"><span class="num">1</span><div><div class="t">Title Goes Here!</div><p>Lorem ipsum dolor sit amet, at laborum nibh duis mauris. Per ultrices lectus sed</p></div></div>
    <div class="toc-item" style="left:118px;top:136px"><span class="num">2</span><div><div class="t">Title Goes Here!</div><p>Lorem ipsum dolor sit amet, at laborum nibh duis mauris. Per ultrices lectus sed</p></div></div>
    <div class="toc-item" style="left:318px;top:86px"><span class="num">3</span><div><div class="t">Title Goes Here!</div><p>Lorem ipsum dolor sit amet, at laborum nibh duis mauris. Per ultrices lectus sed</p></div></div>
    <div class="toc-item" style="left:318px;top:136px"><span class="num">4</span><div><div class="t">Title Goes Here!</div><p>Lorem ipsum dolor sit amet, at laborum nibh duis mauris. Per ultrices lectus sed</p></div></div>
    <div class="toc-item" style="left:318px;top:185px"><span class="num">5</span><div><div class="t">Title Goes Here!</div><p>Lorem ipsum dolor sit amet, at laborum nibh duis mauris. Per ultrices lectus sed</p></div></div>
    <div class="toc-item" style="left:318px;top:234px"><span class="num">6</span><div><div class="t">Title Goes Here!</div><p>Lorem ipsum dolor sit amet, at laborum nibh duis mauris. Per ultrices lectus sed</p></div></div>
    <span class="page-no"></span>
  </section>
  <section class="slide" style="left:609px;top:1828px">
    <div style="left:26px;top:0;width:236px;height:278px;background:linear-gradient(160deg,#c9d6e4,#7f9cbc 55%,#4f76a4)" role="img" aria-label="Photo of a business handshake with network overlay"></div>
    <span class="mark"></span>
    <p class="about-label" style="left:289px;top:84px">About</p>
    <h2 class="about-name" style="left:289px;top:103px">Bellwether Guild<br>Forum</h2>
    <p class="body-text" style="left:289px;top:170px;width:225px">Lorem ipsum dolor sit amet, at laborum nibh duis mauris. Per ultrices lectus sed metus tristique eu. Diam suspendisse ac ipsum maecenas.</p>
    <p class="body-text" style="left:289px;top:205px;width:225px">Eu adipiscing pulvinar eros. Mollis malesuada vel scelerisque, ligula quam non mauris neque eleifend etiam. Tincidunt duis velit lacus phasellus dui vitae, nec eu.</p>
    <span class="page-no"></span>
  </section>

  <!-- Row 5 -->
  <section class="slide" style="left:50px;top:2149px">
    <div class="how-band"></div>
    <span class="mark" style="background:var(--white)"></span>
    <div style="left:279px;top:68px;width:237px;height:186px;background:radial-gradient(circle at 35% 40%,#c47a45 0%,#4a3a3a 35%,#1f2f4c 75%)" role="img" aria-label="Photo of a hand touching a glowing network of people"></div>
    <h2 class="how-heading" style="left:31px;top:98px">How <b>We Do It.</b></h2>
    <ul class="how-list" style="left:31px;top:131px">
      <li>Lorem ipsum dolor sit amet, at laborum nibh duis mauris. Per ultrices lectus sed metus tristique eu. Diam suspendisse ac ipsum maecenas.</li>
      <li>Eu adipiscing pulvinar eros. Mollis malesuada vel scelerisque, ligula quam non mauris neque eleifend etiam. Tincidunt duis velit lacus phasellus dui vitae, nec eu.</li>
    </ul>
    <span class="page-no" style="background:var(--white)"></span>
  </section>
  <section class="slide" style="left:609px;top:2149px">
    <h2 class="heading"><b>Slide Title</b> Goes Here!</h2>
    <span class="mark"></span>
    <div class="feature right-align" style="left:30px;top:101px"><h4>Title Goes Here!</h4><p>Lorem ipsum dolor sit amet, at laborum nibh duis mauris. Per ultrices lectus sed metus tristique eu.</p></div>
    <div class="icon-disc" style="left:208px;top:100px"><svg width="18" height="18" viewBox="0 0 18 18" fill="none" stroke="#fff" stroke-width="1.6"><path d="M9 2a5 5 0 0 0-3 9v2h6v-2a5 5 0 0 0-3-9zM7 16h4"/></svg></div>
    <div class="icon-disc" style="left:297px;top:100px"><svg width="18" height="18" viewBox="0 0 18 18" fill="none" stroke="#fff" stroke-width="1.8"><circle cx="7.5" cy="7.5" r="4.5"/><path d="M11 11l5 5"/></svg></div>
    <div class="feature" style="left:360px;top:101px"><h4>Title Goes Here!</h4><p>Lorem ipsum dolor sit amet, at laborum nibh duis mauris. Per ultrices lectus sed metus tristique eu.</p></div>
    <div class="feature right-align" style="left:30px;top:193px"><h4>Title Goes Here!</h4><p>Lorem ipsum dolor sit amet, at laborum nibh duis mauris. Per ultrices lectus sed metus tristique eu.</p></div>
    <div class="icon-disc" style="left:208px;top:192px"><svg width="18" height="18" viewBox="0 0 18 18" fill="none" stroke="#fff" stroke-width="1.5"><rect x="3" y="2" width="12" height="14" rx="1.5"/><path d="M6 6h6M6 9h6M6 12h6"/></svg></div>
    <div class="icon-disc" style="left:297px;top:192px"><svg width="18" height="18" viewBox="0 0 18 18" fill="none" stroke="#fff" stroke-width="1.8"><path d="M3 15l7-7M11 3a3.5 3.5 0 0 0 4 4l-2 2-4-4zM3 3l12 12"/></svg></div>
    <div class="feature" style="left:360px;top:193px"><h4>Title Goes Here!</h4><p>Lorem ipsum dolor sit amet, at laborum nibh duis mauris. Per ultrices lectus sed metus tristique eu.</p></div>
    <span class="page-no"></span>
  </section>

  <!-- Row 6 -->
  <section class="slide" style="left:50px;top:2471px">
    <h2 class="heading"><b>Slide Title</b> Goes Here!</h2>
    <span class="mark"></span>
    <table class="partner-table">
      <thead><tr><th>Partner Type</th><th>What they do</th><th>How they earn money</th><th>When you use it</th></tr></thead>
      <tbody>
        <tr><td>Referral</td><td>Introduce prospective customers to you</td><td>You pay them a commission when you close the deal</td><td>To incentivize any partner to bring you leads</td></tr>
        <tr><td>Procurement Reseller</td><td>Purchase software on behalf of your end customer</td><td>Charge fees to your end customer</td><td>When required by your customer</td></tr>
        <tr><td>Value added Reseller (VAR)</td><td>Resell your software &amp; services, may combine with their own services and other products</td><td>Margin on resales, value added services around your product</td><td>Increase your reach to partners' customer base and/or other geos</td></tr>
        <tr><td>Distributor</td><td>Recruits and manages a large number of resellers for you</td><td>Margin on resales through VARs</td><td>Scale sales of low touch products</td></tr>
        <tr><td>Global Systems Integrator (GSI)</td><td>IT services &amp; solutions involving many products &amp; services</td><td>Consulting services</td><td>Your product aids delivery of services</td></tr>
        <tr><td>OEM</td><td>License your products to be bundled with their products</td><td>Selling their product that includes yours</td><td>Your product adds value to another vendor's product</td></tr>
      </tbody>
    </table>
    <span class="page-no"></span>
  </section>
  <section class="slide" style="left:609px;top:2471px">
    <h2 class="heading">Partner <b>Complexity</b> and <b>Value Spectrum</b></h2>
    <span class="mark"></span>
    <svg class="deco" viewBox="0 0 541 303">
      <g stroke="#c7ccd3" stroke-width="3"><path d="M58 149H480"/><path d="M63 143l-8 6 8 6M475 143l8 6-8 6" fill="none"/></g>
      <g stroke="#9aa3ae" stroke-width="0.8"><path d="M98 149v56M139 149v80M269 149v56M417 149v80M441 149v56"/></g>
      <g fill="#0f62bd" stroke="#fff" stroke-width="2"><circle cx="98" cy="149" r="6"/><circle cx="139" cy="149" r="6"/><circle cx="269" cy="149" r="6"/><circle cx="417" cy="149" r="6"/><circle cx="441" cy="149" r="6"/></g>
    </svg>
    <p class="spec-label" style="left:56px;top:94px">Low Complexity<br>Quick &amp; Easy<br>Lower Value</p>
    <p class="vendor" style="left:228px;top:102px">RELAYLANE</p>
    <p class="spec-label" style="left:375px;top:94px">High Complexity<br>Longer time to<br>establish Higher<br>Value</p>
    <p class="spec-label" style="left:43px;top:210px">Procurement</p>
    <p class="spec-label" style="left:84px;top:234px">Referral</p>
    <p class="spec-label" style="left:214px;top:210px">Value Added<br>Reseller (VAR)</p>
    <p class="spec-label" style="left:386px;top:210px">OEM</p>
    <p class="spec-label" style="left:362px;top:234px">Global Systems<br>Integrator (GSI)</p>
    <span class="page-no"></span>
  </section>

  <!-- Row 7 -->
  <section class="slide" style="left:50px;top:2793px">
    <h2 class="heading"><b>Slide Title</b> Goes Here!</h2>
    <span class="mark"></span>
    <svg class="deco" viewBox="0 0 541 303"><path d="M0 123H495" stroke="#9fb3cc" stroke-width="1" stroke-dasharray="2 3"/></svg>
    <div class="step-disc" style="left:90px;top:105px">1</div>
    <div class="step-disc" style="left:198px;top:105px">2</div>
    <div class="step-disc" style="left:307px;top:105px">3</div>
    <div class="step-disc" style="left:415px;top:105px">4</div>
    <div class="step" style="left:63px;top:168px"><h4>Title<br>Goes Here!</h4><p>Lorem ipsum dolor sit amet, at laborum nibh duis mauris. Per ultrices lectus sed metus tristique eu.</p></div>
    <div class="step" style="left:171px;top:168px"><h4>Title<br>Goes Here!</h4><p>Lorem ipsum dolor sit amet, at laborum nibh duis mauris. Per ultrices lectus sed metus tristique eu.</p></div>
    <div class="step" style="left:280px;top:168px"><h4>Title<br>Goes Here!</h4><p>Lorem ipsum dolor sit amet, at laborum nibh duis mauris. Per ultrices lectus sed metus tristique eu.</p></div>
    <div class="step" style="left:388px;top:168px"><h4>Title<br>Goes Here!</h4><p>Lorem ipsum dolor sit amet, at laborum nibh duis mauris. Per ultrices lectus sed metus tristique eu.</p></div>
    <span class="page-no"></span>
  </section>
  <section class="slide dark" style="left:609px;top:2793px">
    <div class="brand" style="left:45px;top:125px"><span class="dot"></span><span class="name">Bellwether Guild Forum</span></div>
    <h2 class="contact-h" style="left:45px;top:190px">Contact Us</h2>
    <p class="contact-line" style="left:45px;top:220px"><svg width="9" height="9" viewBox="0 0 10 10" fill="#fff"><path d="M2 1l2 2-1 1.5c.6 1.2 1.3 1.9 2.5 2.5L7 6l2 2-1.5 1.5C4.5 9 1 5.5.5 2.5z"/></svg>555-0142-7788</p>
    <p class="contact-line" style="left:45px;top:235px"><svg width="9" height="9" viewBox="0 0 10 10" fill="none" stroke="#fff" stroke-width="1.2"><circle cx="5" cy="5" r="1.8"/><path d="M6.8 5v1a1.5 1.5 0 0 0 2.5 0V5A4.3 4.3 0 1 0 7 8.8"/></svg>info@bellwetherguild.org</p>
    <p class="contact-line" style="left:45px;top:250px"><svg width="9" height="9" viewBox="0 0 10 10" fill="none" stroke="#fff" stroke-width="0.9"><circle cx="5" cy="5" r="4.2"/><path d="M.8 5h8.4M5 .8c2 2.3 2 6.1 0 8.4M5 .8c-2 2.3-2 6.1 0 8.4"/></svg>www.bellwetherguild.org</p>
  </section>

</main>
</body>
</html>
```